Business Cards Design for the electrical wholesaler: clean bold dynamic :)

We need a business card design that would follow our latest brand guidelines. As an electrical wholesaler we want to bring a fresh look and feel into the industry. The design should be clean bold and dynamic. It should come alive with the renewed energy of our green colour. Our grey colour should keep things balanced and complement the notion of maturity and responsibility. We employ Lato as a corporate font however are not bound by this font and we’re open to interpretation here.

Target Market(s)

Electrical contractors

Industry/Entity Type

Business

Contact Information for Business Card

Logo
Name & Surname: Olena Dovbush
Job Title: Director of Marketing
Email: helen.dovbush@mailvane.example
Cell phone: XXX.XXX.XXXX
Address: 20917 - 87 Ave. Edmonton, AB, Canada. T6K 2R8
Business Phone: 780.555.0187
Website: www.qorvil.example

Font styles to use
Other font styles liked:
• Lato

Requirements
Must have
• Logo & website
Nice to have
• Brand elements - some of them you may find in the attached Brand Guidelines (e.g. three lines on the background signifying "W")

```html
<!DOCTYPE html>
<html lang="en">
<head>
<meta charset="utf-8">
<title>Qorvil Business Cards</title>
<link rel="stylesheet" href="https://fonts.googleapis.com/css2?family=Lato:wght@400;700;900&display=swap">
<style>
  :root {
    --bg: #8c8c8c;
    --card-white: #f1f1f1;
    --brand-green: #86c03f;
    --brand-grey: #4a4b4d;
    --line-grey: #4d4e50;
    --text-white: #ffffff;
  }
  * { margin: 0; padding: 0; box-sizing: border-box; }
  html, body { width: 1200px; height: 942px; overflow: hidden; }
  body {
    background: var(--bg);
    font-family: "Lato", sans-serif;
    position: relative;
  }
  .card {
    position: absolute;
    left: 340px;
    width: 520px;
    height: 300px;
    border-radius: 12px;
    overflow: hidden;
    background: var(--card-white);
    box-shadow: 0 3px 8px rgba(0,0,0,0.25);
  }
  .card--front { top: 150px; }
  .card--back { top: 500px; }
  .card svg.shapes { position: absolute; inset: 0; }

  .holder { position: absolute; left: 34px; top: 58px; }
  .holder__name { color: var(--brand-green); font-weight: 900; font-size: 19px; letter-spacing: 0.2px; }
  .holder__title { color: var(--brand-grey); font-size: 13px; margin-top: 3px; }

  .contact-row {
    position: absolute;
    left: 86px;
    color: var(--text-white);
    font-size: 12px;
    line-height: 16px;
    white-space: nowrap;
  }
  .contact-row--phone { top: 128px; }
  .contact-row--web { top: 171px; }
  .contact-row--address { top: 215px; font-size: 11.5px; line-height: 14px; width: 200px; white-space: normal; }

  .brand-lockup {
    position: absolute;
    right: 44px;
    top: 100px;
    text-align: center;
  }
  .brand-lockup__name { font-weight: 700; font-size: 56px; line-height: 1; color: var(--brand-grey); letter-spacing: -1px; }
  .brand-lockup__tag { font-weight: 700; font-size: 10px; letter-spacing: 1.6px; color: var(--brand-grey); margin-top: 6px; }

  .brand-lockup--back { left: 0; right: 0; top: 68px; }
  .brand-lockup--back .brand-lockup__name { color: var(--text-white); font-size: 70px; }
  .brand-lockup--back .brand-lockup__tag { color: var(--brand-green); font-size: 11px; }

  .website {
    position: absolute;
    left: 0; right: 0; bottom: 20px;
    text-align: center;
    font-size: 13px;
    letter-spacing: 7px;
    color: var(--brand-grey);
  }
  .website__name { color: var(--brand-green); font-weight: 700; }
</style>
</head>
<body>

<section class="card card--front" aria-label="Business card front">
  <svg class="shapes" width="520" height="300" viewBox="0 0 520 300" aria-hidden="true">
    <path d="M0 256 L370 256 Q382 256 390 250 L520 250 L520 300 L0 300 Z" fill="var(--brand-grey)"/>
    <path d="M0 120 L235 120 Q246 120 253 131 L326 236 Q334 249 318 250 L0 252 Z" fill="var(--brand-green)"/>
    <line x1="0" y1="165" x2="274" y2="165" stroke="var(--line-grey)" stroke-width="3"/>
    <line x1="0" y1="208" x2="303" y2="208" stroke="var(--line-grey)" stroke-width="3"/>
    <path d="M52 130 c-3 0 -6 4 -5 8 c2 8 8 15 16 18 c4 1 7 -2 7 -4 l-1 -3 l-5 -2 l-2 2 c-3 -1 -7 -5 -8 -8 l2 -2 l-2 -5 z" fill="var(--text-white)"/>
    <g fill="none" stroke="var(--text-white)" stroke-width="1.6">
      <circle cx="58" cy="187" r="12"/>
      <ellipse cx="58" cy="187" rx="5" ry="12"/>
      <line x1="46" y1="187" x2="70" y2="187"/>
      <path d="M48 181 H68 M48 193 H68"/>
    </g>
    <path d="M60 217 a9 9 0 0 1 9 9 c0 7 -9 16 -9 16 s-9 -9 -9 -16 a9 9 0 0 1 9 -9 z" fill="var(--text-white)"/>
    <circle cx="60" cy="226" r="3.5" fill="var(--brand-green)"/>
  </svg>

  <div class="holder">
    <div class="holder__name">OLENA DOVBUSH</div>
    <div class="holder__title">Director of Marketing</div>
  </div>

  <div class="contact-row contact-row--phone">780.555.0187<br>780.555.0187</div>
  <div class="contact-row contact-row--web">helen.dovbush@mailvane.example<br>www.qorvil.example</div>
  <div class="contact-row contact-row--address">20917 - 87 Ave. Edmonton, AB, Canada. T6K 2R8</div>

  <div class="brand-lockup">
    <div class="brand-lockup__name">qorvil</div>
    <div class="brand-lockup__tag">ELECTRICAL WHOLESALERS</div>
  </div>
</section>

<section class="card card--back" aria-label="Business card back">
  <svg class="shapes" width="520" height="300" viewBox="0 0 520 300" aria-hidden="true">
    <path d="M0 0 H520 V150 H440 L388 252 H132 L80 150 H0 Z" fill="var(--brand-grey)"/>
    <path d="M0 150 H80 L132 252 H388 L440 150 H520" fill="none" stroke="var(--brand-green)" stroke-width="5" stroke-linejoin="round"/>
  </svg>

  <div class="brand-lockup brand-lockup--back">
    <div class="brand-lockup__name">qorvil</div>
    <div class="brand-lockup__tag">ELECTRICAL WHOLESALERS</div>
  </div>

  <div class="website">www.<span class="website__name">qorvil</span>.example</div>
</section>

</body>
</html>
```